Postcard Design

A house cleaning business. Focus on time saving and stress free. Free estimates. Want it to state that we can make your home sparkle or shine. I have been using the colors purple and black in the logo which I will attach.

Reason: I need a few more days to decide on this. Thank you

Industry/Entity Type

House

Colors
886aae
6b449b

Requirements
Must have
• website www.tidwellhavenhomes.us
phone # 555-390-6172

```html
<!DOCTYPE html>
<html lang="en">
<head>
<meta charset="utf-8">
<title>Tidwell Haven Homes – Postcard</title>
<link href="https://fonts.googleapis.com/css2?family=Tinos:ital,wght@0,400;0,700;1,700&family=Arimo:wght@400;700&family=Kaushan+Script&display=swap" rel="stylesheet">
<style>
:root{
  --purple-light:#9d6ca9;
  --purple:#6b449b;
  --purple-mid:#886aae;
  --purple-deep:#2e1640;
  --ink:#1a1a1a;
  --silver:#cfcfcf;
  --white:#ffffff;
  --label:#555555;
}
*{margin:0;padding:0;box-sizing:border-box}
html,body{width:1200px;height:1173px;overflow:hidden;background:var(--white)}
body{position:relative;font-family:"Tinos",serif}
.side-label{position:absolute;font-family:"Arimo",sans-serif;font-size:24px;color:var(--label)}
.label-front{left:241px;top:8px}
.label-back{left:241px;top:586px}
.card{position:absolute;border:1px solid #333;overflow:hidden;background:var(--white)}
.card-front{left:233px;top:42px;width:741px;height:541px}
.card-back{left:234px;top:615px;width:742px;height:543px}
.card svg.art{position:absolute;left:0;top:0}
.abs{position:absolute}
.tagline{left:24px;top:242px;font-family:"Kaushan Script",cursive;font-size:23px;color:var(--purple);letter-spacing:.5px}
.pitch{left:40px;top:278px;width:330px;text-align:center;font-size:19px;line-height:25px;color:var(--ink)}
.duster{background:linear-gradient(160deg,#2a2a2a,#0d0d0d);border-radius:40% 55% 45% 50%}
.duster-front{left:58px;top:345px;width:74px;height:70px}
.phone-pill{background:var(--purple);border-radius:50%;color:var(--white);font-weight:700;text-align:center;box-shadow:4px 8px 0 #b79cc4}
.phone-front{left:87px;top:370px;width:214px;height:58px;font-size:22px;line-height:26px;padding-top:3px}
.brand{color:var(--purple);font-family:"Tinos",serif;font-weight:700;text-align:center}
.brand-front{left:395px;top:230px;width:320px;font-size:40px;line-height:46px}
.web-front{right:30px;top:474px;font-size:20px;font-weight:700;color:var(--white)}
.duster-back{left:20px;top:145px;width:66px;height:52px}
.phone-back{left:30px;top:182px;width:160px;height:42px;font-size:16px;line-height:19px;padding-top:2px;box-shadow:3px 6px 0 #b79cc4}
.brand-back{left:190px;top:118px;width:175px;font-size:22px;line-height:26px}
.estimates{left:0;top:275px;width:373px;text-align:center;font-size:25px;font-weight:700;color:var(--purple)}
.web-back{left:0;top:308px;width:373px;text-align:center;font-family:"Arimo",sans-serif;font-size:22px;font-weight:700;color:var(--purple)}
.address-side{left:373px;top:0;width:369px;height:543px;background:var(--white)}
.stamp-box{left:260px;top:24px;width:92px;height:100px;border:1px solid #888}
.address-line{left:28px;width:292px;height:1px;background:#999}
</style>
</head>
<body>
<div class="side-label label-front">front</div>
<div class="side-label label-back">back</div>

<section class="card card-front">
  <svg class="art" width="741" height="541" viewBox="0 0 741 541" aria-hidden="true">
    <defs>
      <linearGradient id="bodyFront" x1="0" y1="0" x2="0" y2="1">
        <stop offset="0" stop-color="#ffffff"/><stop offset="1" stop-color="#d6d6d6"/>
      </linearGradient>
      <linearGradient id="silverFront" x1="0" y1="0" x2="1" y2="0">
        <stop offset="0" stop-color="#9a9a9a"/><stop offset=".5" stop-color="#f2f2f2"/><stop offset="1" stop-color="#b0b0b0"/>
      </linearGradient>
      <clipPath id="bodyClipFront"><path d="M0 225 C260 232 480 160 741 150 L741 540 L0 540Z"/></clipPath>
    </defs>
    <rect width="741" height="541" fill="var(--purple-light)"/>
    <path d="M0 88 C250 105 460 35 741 132 L741 541 L0 541Z" fill="var(--purple)"/>
    <path d="M0 118 C260 145 470 70 741 145 L741 541 L0 541Z" fill="var(--purple-deep)"/>
    <path d="M0 192 C260 212 480 110 741 140 L741 541 L0 541Z" fill="url(#silverFront)"/>
    <path d="M0 222 C260 230 480 158 741 150 L741 541 L0 541Z" fill="url(#bodyFront)"/>
    <line x1="0" y1="225" x2="130" y2="225" stroke="#111" stroke-width="2"/>
    <g clip-path="url(#bodyClipFront)">
      <circle cx="612" cy="300" r="250" fill="var(--white)" stroke="var(--purple)" stroke-width="7"/>
    </g>
    <path d="M0 440 C220 478 470 470 741 402 L741 541 L0 541Z" fill="var(--purple)"/>
    <path d="M0 440 C220 470 470 458 741 402" fill="none" stroke="#111" stroke-width="3"/>
    <path d="M0 470 C260 515 520 500 741 498" fill="none" stroke="#e6e6e6" stroke-width="10"/>
    <path d="M0 478 C260 522 520 508 741 505 L741 541 L0 541Z" fill="var(--purple-light)"/>
    <g fill="#ffffff" opacity=".85">
      <circle cx="70" cy="18" r="3"/><circle cx="155" cy="26" r="4"/><circle cx="235" cy="14" r="2"/>
      <circle cx="340" cy="25" r="4"/><circle cx="390" cy="50" r="2"/><circle cx="470" cy="35" r="3"/>
      <circle cx="520" cy="68" r="2"/><circle cx="600" cy="40" r="2"/><circle cx="690" cy="55" r="3"/>
      <circle cx="130" cy="80" r="3"/><circle cx="280" cy="60" r="2"/><circle cx="600" cy="420" r="3"/>
      <circle cx="690" cy="420" r="4"/><circle cx="40" cy="505" r="3"/><circle cx="160" cy="525" r="4"/>
      <circle cx="300" cy="515" r="3"/><circle cx="460" cy="520" r="2"/><circle cx="660" cy="515" r="3"/>
    </g>
  </svg>
  <p class="abs tagline">Save you time and your stress!</p>
  <p class="abs pitch">Free estimates.<br>Want it to state that we can make your home sparkle or shine!</p>
  <div class="abs duster duster-front" role="img" aria-label="Black feather duster silhouette"></div>
  <div class="abs phone-pill phone-front">phone<br>555-390-6172</div>
  <p class="abs brand brand-front">Tidwell Haven<br>Homes</p>
  <p class="abs web-front">www.tidwellhavenhomes.us</p>
</section>

<section class="card card-back">
  <svg class="art" width="373" height="543" viewBox="0 0 373 543" aria-hidden="true">
    <defs>
      <linearGradient id="bodyBack" x1="0" y1="0" x2="1" y2="1">
        <stop offset="0" stop-color="#ffffff"/><stop offset="1" stop-color="#cfcfcf"/>
      </linearGradient>
      <linearGradient id="silverBack" x1="0" y1="0" x2="1" y2="0">
        <stop offset="0" stop-color="#9a9a9a"/><stop offset=".5" stop-color="#f2f2f2"/><stop offset="1" stop-color="#b0b0b0"/>
      </linearGradient>
      <clipPath id="bodyClipBack"><path d="M0 118 C140 110 250 60 373 78 L373 470 L0 470Z"/></clipPath>
    </defs>
    <rect width="373" height="543" fill="var(--purple-light)"/>
    <path d="M0 50 C130 62 240 20 373 58 L373 543 L0 543Z" fill="var(--purple)"/>
    <path d="M0 65 C140 80 250 35 373 68 L373 543 L0 543Z" fill="var(--purple-deep)"/>
    <path d="M0 100 C140 105 250 50 373 72 L373 543 L0 543Z" fill="url(#silverBack)"/>
    <path d="M0 118 C140 110 250 60 373 78 L373 543 L0 543Z" fill="url(#bodyBack)"/>
    <g clip-path="url(#bodyClipBack)">
      <circle cx="280" cy="150" r="95" fill="var(--white)" stroke="var(--purple)" stroke-width="4"/>
    </g>
    <path d="M0 468 C130 490 250 470 373 460 L373 543 L0 543Z" fill="var(--purple)"/>
    <path d="M0 470 C130 490 250 472 373 462" fill="none" stroke="#111" stroke-width="3"/>
    <path d="M0 500 C140 520 260 505 373 510" fill="none" stroke="#e6e6e6" stroke-width="7"/>
    <path d="M0 506 C140 526 260 512 373 516 L373 543 L0 543Z" fill="var(--purple-light)"/>
    <g fill="#ffffff" opacity=".85">
      <circle cx="40" cy="15" r="2"/><circle cx="85" cy="10" r="3"/><circle cx="130" cy="30" r="2"/>
      <circle cx="190" cy="15" r="2"/><circle cx="250" cy="25" r="3"/><circle cx="310" cy="12" r="2"/>
      <circle cx="60" cy="525" r="2"/><circle cx="200" cy="530" r="3"/><circle cx="330" cy="528" r="2"/>
    </g>
  </svg>
  <div class="abs duster duster-back" role="img" aria-label="Black feather duster silhouette"></div>
  <div class="abs phone-pill phone-back">phone<br>555-390-6172</div>
  <p class="abs brand brand-back">Tidwell Haven<br>Homes</p>
  <p class="abs estimates">FREE ESTIMATES</p>
  <p class="abs web-back">www.tidwellhavenhomes.us</p>
  <div class="abs address-side">
    <div class="abs stamp-box"></div>
    <div class="abs address-line" style="top:331px"></div>
    <div class="abs address-line" style="top:384px"></div>
    <div class="abs address-line" style="top:440px"></div>
  </div>
</section>
</body>
</html>
```